Handyman home maintenance postcard

We would like the postcard to state what we do : Painting, plumbing, electrical, flooring, carpentry, drywall, fencing, windows and more. We would also like our promotion to state : First four hours of work is only $299. Additional hours are 25% off our regular rate of $110 an hour. Rate includes two expert handymen working to complete your job.

Target Market(s)

30-75

Industry/Entity Type

Home maintenance

```html
<!DOCTYPE html>
<html lang="en">
<head>
<meta charset="utf-8">
<title>Steadfast Home Repair – Postcard</title>
<link rel="stylesheet" href="https://fonts.googleapis.com/css2?family=Montserrat:wght@400;500;600;700;800;900&display=swap">
<style>
  :root{
    --navy:#1a2b6b;
    --navy-deep:#12205a;
    --blue:#2f5bb7;
    --orange:#f7931e;
    --orange-deep:#f26b0f;
    --ink:#2b2b2b;
    --grey:#555a66;
    --page:#d6d6d6;
    --white:#ffffff;
  }
  *{box-sizing:border-box;margin:0;padding:0}
  html,body{width:1200px;height:2602px;overflow:hidden}
  body{background:var(--page);font-family:'Montserrat',sans-serif;position:relative;color:var(--ink)}
  .card{position:absolute;left:98px;width:1004px;height:670px;background:var(--white);overflow:hidden;box-shadow:0 14px 22px rgba(0,0,0,.35)}
  .card--front{top:972px}
  .card--back{top:1724px}
  .abs{position:absolute}

  /* brand */
  .brand{display:flex;align-items:center;gap:12px;font-weight:800;color:var(--navy);white-space:nowrap}
  .brand__dot{width:22px;height:22px;border-radius:50%;background:var(--orange);flex:none}

  /* front */
  .front-art{left:0;top:0;width:1004px;height:670px}
  .front-brand{left:48px;top:42px;font-size:34px}
  .headline{left:44px;top:138px;font-size:40px;font-weight:800;line-height:45px;color:var(--navy-deep)}
  .headline em{font-style:normal;color:var(--blue)}
  .tagline{left:45px;top:233px;font-size:17px;font-weight:500;color:var(--grey)}
  .estimate{display:flex;align-items:center;height:34px;border-radius:17px;background:var(--navy);color:var(--white);font-weight:600;overflow:hidden;white-space:nowrap}
  .estimate b{font-weight:800}
  .estimate__label{padding:0 8px 0 12px}
  .estimate__phone{display:flex;align-items:center;gap:6px;background:var(--orange);height:100%;padding:0 12px 0 6px;border-radius:17px;font-weight:800}
  .estimate__icon{width:22px;height:22px;border-radius:50%;background:var(--white);display:flex;align-items:center;justify-content:center}
  .front-estimate{left:48px;top:272px;font-size:16px}
  .url{font-weight:600;color:var(--navy-deep);white-space:nowrap}
  .url span{color:var(--orange-deep)}
  .front-url{left:52px;top:313px;font-size:18px}
  .offer{left:240px;top:508px;width:210px;text-align:center;font-weight:800}
  .offer__lead{color:var(--orange);font-size:17px;line-height:21px}
  .offer__lead small{display:block;color:var(--white);font-size:17px}
  .offer__price{color:var(--orange);font-size:74px;line-height:84px;font-weight:900;letter-spacing:-1px}
  .offer-rule{left:472px;top:520px;width:2px;height:110px;background:rgba(255,255,255,.6)}
  .perks{left:505px;top:510px;width:440px;list-style:none;color:var(--white);font-size:20px;font-weight:500;line-height:24px}
  .perks li{position:relative;padding-left:28px}
  .perks li:first-child{padding-bottom:14px;margin-bottom:22px;border-bottom:2px solid rgba(255,255,255,.75)}
  .perks li svg{position:absolute;left:0;top:4px}
  .perks strong{color:var(--orange);font-weight:700}

  /* back */
  .back-art{left:0;top:0;width:1004px;height:670px}
  .services-tag{left:125px;top:42px;width:190px;height:36px;border-radius:18px;background:var(--white);color:var(--navy);font-size:22px;font-weight:700;text-align:center;line-height:36px}
  .services{left:47px;top:98px;display:grid;grid-template-columns:186px 270px;row-gap:22px;list-style:none;color:var(--white);font-size:22px;font-weight:500}
  .services li{display:flex;align-items:center;gap:13px;height:26px;white-space:nowrap}
  .services i{width:25px;height:25px;background:var(--orange);border-radius:3px;flex:none;border:2px solid #ffd19a}
  .features{left:42px;top:325px;display:flex;gap:10px;list-style:none;font-size:13px;font-weight:700;color:var(--navy);line-height:17px}
  .features li{display:flex;align-items:center;gap:8px;padding-right:10px;border-right:1px solid #b9bccb}
  .features li:last-child{border:none}
  .about{left:45px;top:405px;width:412px}
  .about h2{display:flex;align-items:center;gap:10px;font-size:26px;font-weight:800;color:#2a1e10}
  .about h2::after{content:"";flex:1;height:2px;background:#3a2a14}
  .about p{margin-top:14px;font-size:13.6px;line-height:19.5px;text-align:justify;color:#2a1e10}
  .address{left:45px;top:620px;display:flex;gap:8px;font-size:13px;font-weight:700;color:var(--navy);line-height:17px}
  .back-brand{left:542px;top:86px;font-size:21px;gap:8px}
  .back-brand .brand__dot{width:18px;height:18px}
  .stamp{left:860px;top:52px;width:108px;height:98px;border:1.5px solid #555}
  .address-line{left:634px;width:334px;height:1.5px;background:#555}
  .back-estimate{left:552px;top:562px;height:42px;border-radius:21px;font-size:18px}
  .back-estimate .estimate__phone{border-radius:21px}
  .back-url{left:558px;top:612px;font-size:21px}
</style>
</head>
<body>

<!-- FRONT -->
<section class="card card--front" aria-label="Postcard front">
  <svg class="abs front-art" viewBox="0 0 1004 670" width="1004" height="670">
    <defs>
      <linearGradient id="photoFade" x1="0" x2="1" y1="0" y2="0">
        <stop offset="0" stop-color="#ffffff" stop-opacity="1"/>
        <stop offset=".38" stop-color="#e6e9ee" stop-opacity=".6"/>
        <stop offset=".7" stop-color="#9fb1c8"/>
        <stop offset="1" stop-color="#4d6a94"/>
      </linearGradient>
      <linearGradient id="swoosh" x1="0" x2="1">
        <stop offset="0" stop-color="#f7931e"/>
        <stop offset=".5" stop-color="#ffb84d"/>
        <stop offset="1" stop-color="#f26b0f"/>
      </linearGradient>
    </defs>
    <rect x="330" y="0" width="674" height="470" fill="url(#photoFade)" role="img" aria-label="Photo of a handyman in a blue cap fitting a water filter under a sink"/>
    <path d="M0 318 Q500 640 1004 318 L1004 670 L0 670 Z" fill="url(#swoosh)"/>
    <path d="M0 336 Q500 668 1004 336 L1004 670 L0 670 Z" fill="var(--navy-deep)"/>
    <path d="M0 336 Q500 668 1004 336" fill="none" stroke="#ffffff" stroke-width="2" opacity=".7"/>
    <rect x="18" y="345" width="215" height="325" rx="6" fill="#3b5aa8" role="img" aria-label="Photo of a smiling worker in an orange hard hat holding a drill"/>
  </svg>

  <div class="abs brand front-brand"><span class="brand__dot"></span>Steadfast Home Repair</div>
  <h1 class="abs headline">Trusted Handyman<br>&amp; <em>Repair</em> Services</h1>
  <p class="abs tagline">Your Expert Go-To For Home Repairs.</p>
  <div class="abs estimate front-estimate">
    <span class="estimate__label">Get <b>Free Estimate Call</b></span>
    <span class="estimate__phone"><span class="estimate__icon"><svg width="12" height="12" viewBox="0 0 24 24"><path d="M6.6 10.8a15 15 0 0 0 6.6 6.6l2.2-2.2c.3-.3.7-.4 1-.2 1.1.4 2.3.6 3.6.6.6 0 1 .4 1 1V20c0 .6-.4 1-1 1A17 17 0 0 1 3 4c0-.6.4-1 1-1h3.5c.6 0 1 .4 1 1 0 1.3.2 2.5.6 3.6.1.3 0 .7-.2 1z" fill="#1a2b6b"/></svg></span>310 555 0148</span>
  </div>
  <p class="abs url front-url">www.<span>steadfasthomerepair</span>.com</p>

  <div class="abs offer">
    <p class="offer__lead">FIRST FOUR HOURS<small>OF WORK IS ONLY</small></p>
    <p class="offer__price">$299</p>
  </div>
  <div class="abs offer-rule"></div>
  <ul class="abs perks">
    <li><svg width="18" height="18" viewBox="0 0 20 20"><circle cx="10" cy="10" r="8" fill="none" stroke="#fff" stroke-width="1.6"/><path d="M6 10l3 3 6-6" fill="none" stroke="#fff" stroke-width="1.8"/></svg>Additional hours are <strong>25% off</strong><br>our regular rate of <strong>$110</strong> an hour.</li>
    <li><svg width="18" height="18" viewBox="0 0 20 20"><circle cx="10" cy="10" r="8" fill="none" stroke="#fff" stroke-width="1.6"/><path d="M6 10l3 3 6-6" fill="none" stroke="#fff" stroke-width="1.8"/></svg>Rate includes <strong>two expert handymen</strong><br>working to complete your job.</li>
  </ul>
</section>

<!-- BACK -->
<section class="card card--back" aria-label="Postcard back">
  <svg class="abs back-art" viewBox="0 0 1004 670" width="1004" height="670">
    <defs>
      <linearGradient id="aboutBand" x1="0" x2="1">
        <stop offset="0" stop-color="#f7931e"/>
        <stop offset="1" stop-color="#fbb040"/>
      </linearGradient>
    </defs>
    <rect x="0" y="0" width="560" height="310" fill="var(--navy-deep)"/>
    <rect x="0" y="0" width="560" height="310" fill="#24388a" opacity=".35" role="img" aria-label="Faint photo of a worker using tools, tinted blue"/>
    <rect x="0" y="310" width="560" height="80" fill="#ffffff"/>
    <rect x="0" y="390" width="560" height="222" fill="url(#aboutBand)"/>
    <path d="M418 0 Q640 300 420 670 L1004 670 L1004 0 Z" fill="var(--orange)"/>
    <path d="M440 0 Q650 300 432 670 L1004 670 L1004 0 Z" fill="#ffffff"/>
  </svg>

  <div class="abs services-tag">What we do</div>
  <ul class="abs services">
    <li><i></i>Painting</li><li><i></i>Carpentry</li>
    <li><i></i>Plumbing</li><li><i></i>Drywall</li>
    <li><i></i>Electrical</li><li><i></i>Fencing</li>
    <li><i></i>Flooring</li><li><i></i>windows and more</li>
  </ul>

  <ul class="abs features">
    <li><svg width="38" height="38" viewBox="0 0 40 40"><circle cx="20" cy="20" r="15" fill="none" stroke="var(--orange)" stroke-width="2.5"/><path d="M20 11v10l6 4" fill="none" stroke="var(--navy)" stroke-width="2.5"/></svg><span>20+ years of<br>experience</span></li>
    <li><svg width="38" height="38" viewBox="0 0 40 40"><rect x="5" y="17" width="7" height="16" fill="none" stroke="var(--orange)" stroke-width="2.5"/><path d="M12 19l7-11c2 0 3 2 2 5l-1 4h10c2 0 3 2 2 4l-3 10c-1 2-2 2-3 2H12" fill="none" stroke="var(--orange)" stroke-width="2.5"/></svg><span>Reliable &amp;<br>Quality Service</span></li>
    <li><svg width="30" height="38" viewBox="0 0 30 40"><circle cx="15" cy="15" r="11" fill="none" stroke="var(--navy)" stroke-width="2.2"/><circle cx="15" cy="15" r="4" fill="var(--orange)"/><path d="M10 28h10M11 33h8" stroke="var(--navy)" stroke-width="2.2"/></svg><span>Skilled &amp; Trained<br>Personel</span></li>
  </ul>

  <div class="abs about">
    <h2>Who We Are</h2>
    <p>Steadfast Home Repair strives to be your go-to for home repairs. We have many years of experience in all facets of home repair and maintenance. Whether you are looking to repair that running toilet, replace that tired looking floor or give your home’s exterior or interior a fresh new color, we can get it done for you. On time, neatly and at a reasonable price.</p>
  </div>

  <div class="abs address">
    <svg width="12" height="16" viewBox="0 0 12 16"><path d="M6 1a5 5 0 0 0-5 5c0 4 5 9 5 9s5-5 5-9a5 5 0 0 0-5-5z" fill="none" stroke="var(--navy)" stroke-width="1.4"/><circle cx="6" cy="6" r="1.8" fill="var(--navy)"/></svg>
    <span>4120 Maple Ridge Ave, #12, Los Angeles,<br>California, 90016</span>
  </div>

  <div class="abs brand back-brand"><span class="brand__dot"></span>Steadfast Home Repair</div>
  <div class="abs stamp"></div>
  <div class="abs address-line" style="top:320px"></div>
  <div class="abs address-line" style="top:390px"></div>
  <div class="abs address-line" style="top:460px"></div>

  <div class="abs estimate back-estimate">
    <span class="estimate__label">Get <b>Free Estimate Call</b></span>
    <span class="estimate__phone"><span class="estimate__icon"><svg width="13" height="13" viewBox="0 0 24 24"><path d="M6.6 10.8a15 15 0 0 0 6.6 6.6l2.2-2.2c.3-.3.7-.4 1-.2 1.1.4 2.3.6 3.6.6.6 0 1 .4 1 1V20c0 .6-.4 1-1 1A17 17 0 0 1 3 4c0-.6.4-1 1-1h3.5c.6 0 1 .4 1 1 0 1.3.2 2.5.6 3.6.1.3 0 .7-.2 1z" fill="#1a2b6b"/></svg></span>310 555 0148</span>
  </div>
  <p class="abs url back-url">www.<span>steadfasthomerepair</span>.com</p>
</section>

</body>
</html>
```